Business cards

Design business cards for our company. Just a straight, business like design with the logo, name, function and contact details

Target Market(s)

We are a innovative technological company active in water treatment

Industry/Entity Type

Water management

Contact Information for Business Card

Name, Function, email, telephone number, link to website

```html
<!DOCTYPE html>
<html lang="en">
<head>
<meta charset="utf-8">
<title>Tidewell – Business Card</title>
<link href="https://fonts.googleapis.com/css2?family=Montserrat:wght@400;500;700&display=swap" rel="stylesheet">
<style>
  :root{
    --stage:#e7e0d6;
    --frost:#f1f3f5;
    --frost-edge:#d9dde1;
    --ocean:#1f7fa6;
    --ocean-deep:#16698d;
    --ocean-bright:#2a9ad0;
    --crescent:#7a7470;
    --gold:#d9b98a;
    --gold-soft:#ead8bb;
    --brand:#2f8fc4;
  }
  *{margin:0;padding:0;box-sizing:border-box}
  html,body{width:1200px;height:897px;overflow:hidden;background:var(--stage)}
  .canvas{position:relative;width:1200px;height:897px}
  .card{position:absolute;left:80px;top:165px;width:1040px;height:567px;border-radius:26px;overflow:hidden;
        box-shadow:0 10px 30px rgba(0,0,0,.15)}
  .card-shapes{position:absolute;inset:0;width:100%;height:100%}
  .card-text{position:absolute;font-family:'Montserrat',sans-serif}
  .brand{left:58px;top:255px;display:flex;align-items:center;gap:14px}
  .brand-name{font-size:42px;font-weight:500;color:var(--brand);letter-spacing:.5px}
  .brand-dot{width:26px;height:26px;border-radius:50%;background:var(--brand)}
  .details{left:580px;top:112px;color:var(--gold-soft)}
  .person-name{font-size:33px;font-weight:700;color:var(--gold);letter-spacing:1px;line-height:1.1}
  .person-role{font-size:21px;font-weight:400;line-height:1.3}
  .divider{width:20px;height:2px;background:var(--gold-soft);margin:26px 0 30px}
  .address{font-size:22px;line-height:1.35;letter-spacing:.5px}
  .contacts{list-style:none;font-size:22px;letter-spacing:.5px}
  .contacts li{display:flex;align-items:center;gap:10px;height:39px}
  .contacts svg{width:18px;height:18px;fill:var(--gold-soft)}
</style>
</head>
<body>
<div class="canvas">
  <div class="card">
    <svg class="card-shapes" viewBox="0 0 1040 567" preserveAspectRatio="none">
      <defs>
        <linearGradient id="frostFill" x1="0" y1="0" x2="1" y2="1">
          <stop offset="0" stop-color="#f6f7f8"/>
          <stop offset="1" stop-color="#e6e2df"/>
        </linearGradient>
        <linearGradient id="oceanFill" x1="0" y1="0" x2="1" y2="0">
          <stop offset="0" stop-color="#16698d"/>
          <stop offset=".55" stop-color="#1f84b3"/>
          <stop offset=".75" stop-color="#2a9ad0"/>
          <stop offset="1" stop-color="#1f7fa6"/>
        </linearGradient>
      </defs>
      <rect class="frost-panel" width="1040" height="567" fill="url(#frostFill)"/>
      <path class="crescent" d="M372,0 Q560,283 372,567 L460,567 Q600,283 460,0 Z" fill="var(--crescent)" opacity=".85"/>
      <path class="ocean-panel" d="M460,0 Q600,283 460,567 L1040,567 L1040,0 Z" fill="url(#oceanFill)"/>
      <path class="ocean-edge" d="M460,0 Q600,283 460,567" fill="none" stroke="var(--gold)" stroke-width="3"/>
    </svg>

    <div class="card-text brand">
      <span class="brand-name">Tidewell</span>
      <span class="brand-dot"></span>
    </div>

    <div class="card-text details">
      <h1 class="person-name">DANIEL HART</h1>
      <p class="person-role">CEO/Founder</p>
      <div class="divider"></div>
      <p class="address">412 Harbor Lane<br>Westfield AB 3190</p>
      <div class="divider"></div>
      <ul class="contacts">
        <li><svg viewBox="0 0 24 24"><path d="M6.6 10.8a15 15 0 0 0 6.6 6.6l2.2-2.2a1 1 0 0 1 1-.25 11.4 11.4 0 0 0 3.6.57 1 1 0 0 1 1 1V20a1 1 0 0 1-1 1A17 17 0 0 1 3 4a1 1 0 0 1 1-1h3.5a1 1 0 0 1 1 1c0 1.25.2 2.45.57 3.6a1 1 0 0 1-.25 1z"/></svg>555-014-2271</li>
        <li><svg viewBox="0 0 24 24"><path d="M3 6h18v12H3z M3 6l9 7 9-7" fill="none" stroke="#ead8bb" stroke-width="2"/></svg>info@tidewellwater.com</li>
        <li><svg viewBox="0 0 24 24"><circle cx="12" cy="12" r="9" fill="none" stroke="#ead8bb" stroke-width="2"/><path d="M3 12h18M12 3c3 3 3 15 0 18M12 3c-3 3-3 15 0 18" fill="none" stroke="#ead8bb" stroke-width="1.6"/></svg>www.tidewellwater.com</li>
      </ul>
    </div>
  </div>
</div>
</body>
</html>
```